Zentrix Banner Grid Ads for Custom Software Company

We need some images for display on the Zentrix Banner Grid. Need a collection of them at different sizes.

This is for a custom software development company that specializes in small to medium size businesses.

PLEASE PLEASE PLEASE GET CREATIVE! That is the point! Something very typical and plain will not win!

Target Market(s)

Small and Medium sized businesses looking for custom software development services

Industry/Entity Type

Computer Software

Font styles to use
Serif
Sans Serif

Requirements
Must have
• Medium Rectangle (300×250)
• Large Rectangle (336×280)
• Leaderboard (728×90)
• Half Page (300×600)
• Large Mobile Banner (320×100)
• Needs to stand out, but not be obnoxious
• Needs to flow with the website design and colors (does not need to be the same colors, just needs to work together)
• Must have specific call to action (schedule appointment or read more are options, but feel free to make up more)
Nice to have
• Logo integration
• Adobe Illustrator files with artboards/exports for the different sizes
Should not have
• Should not have more than 20% text
• Don't steal from the slides on the website. We want "read more" to mean read more, not more of the same.

```html
<!DOCTYPE html>
<html lang="en">
<head>
<meta charset="utf-8">
<title>Velquor Display Banner Set</title>
<link rel="stylesheet" href="https://fonts.googleapis.com/css2?family=Roboto:ital,wght@0,400;0,700;0,900;1,400;1,700&display=swap">
<style>
:root{
  --page:#dfe3e6;
  --teal-deep:#35c1c8;
  --teal:#4fcfd4;
  --teal-light:#8fe3e4;
  --cloud:#f3f5f5;
  --ink:#262a2c;
  --white:#ffffff;
  --cta-top:#2a7fd0;
  --cta-bottom:#0d4c98;
  --brand:#1b63b0;
}
*{margin:0;padding:0;box-sizing:border-box}
html,body{width:1200px;height:900px;overflow:hidden}
body{background:var(--page);font-family:"Roboto",Arial,sans-serif;position:relative}
.banner{position:absolute;overflow:hidden;box-shadow:0 4px 14px rgba(0,0,0,.18);
  background:linear-gradient(180deg,var(--teal-deep) 0%,var(--teal) 40%,var(--teal-light) 55%,#e6f6f6 72%,var(--cloud) 100%)}
.banner>*{position:absolute}
.line{display:block;white-space:nowrap;line-height:1;text-transform:uppercase}
.light{font-style:italic;font-weight:400}
.bold{font-weight:700}
.on-teal{color:var(--white)}
.dark{color:var(--ink)}
.illustration{border-radius:50%;
  background:radial-gradient(circle at 50% 45%,#ffffff 0%,#d7eef4 35%,rgba(143,227,228,.5) 65%,rgba(143,227,228,0) 72%)}
.divider{height:1px;background:rgba(255,255,255,.45)}
.cta{background:linear-gradient(180deg,var(--cta-top),var(--cta-bottom));color:var(--white);
  text-transform:uppercase;text-align:center;display:flex;flex-direction:column;justify-content:center;
  line-height:1.05;box-shadow:0 3px 5px rgba(0,0,0,.25);border-radius:2px}
.cta .top{font-weight:400}
.cta .bottom{font-weight:700}
.brand{display:flex;align-items:center;color:var(--brand);font-weight:400;white-space:nowrap}
.brand .mark{background:var(--brand);margin-right:.3em;display:inline-block}

/* Leaderboard */
.leaderboard{left:64px;top:111px;width:723px;height:89px;
  background:linear-gradient(90deg,var(--teal-deep) 0%,var(--teal) 50%,var(--teal-light) 70%,var(--cloud) 78%,var(--cloud) 100%)}
.leaderboard .headline{left:18px;top:17px;font-size:26px}
.leaderboard .headline .line+.line{margin-top:4px}
.leaderboard .v-divider{left:278px;top:14px;width:1px;height:60px;background:rgba(255,255,255,.45)}
.leaderboard .results{left:302px;top:17px}
.leaderboard .results .light{font-size:23px}
.leaderboard .results .bold{font-size:38px;margin-top:1px}
.leaderboard .illustration{left:470px;top:2px;width:90px;height:85px}
.leaderboard .cta{left:589px;top:12px;width:110px;height:29px}
.leaderboard .cta .top,.leaderboard .cta .bottom{font-size:10px}
.leaderboard .brand{left:597px;top:57px;font-size:21px}
.leaderboard .brand .mark{width:22px;height:22px}

/* Half page */
.half-page{left:66px;top:225px;width:273px;height:545px}
.half-page .headline{left:42px;top:37px}
.half-page .headline .light{font-size:30px}
.half-page .headline .bold{font-size:30px;margin-top:-1px}
.half-page .headline .bold.big{font-size:44px}
.half-page .headline .gap{margin-top:20px}
.half-page .divider{left:36px;top:216px;width:200px}
.half-page .illustration{left:60px;top:225px;width:170px;height:170px}
.half-page .results{left:32px;top:255px;text-align:center;width:210px}
.half-page .results .light{font-size:30px}
.half-page .results .bold{font-size:46px;margin-top:4px}
.half-page .cta{left:78px;top:414px;width:120px;height:32px}
.half-page .cta span{font-size:12px}
.half-page .brand{left:52px;top:482px;font-size:30px}
.half-page .brand .mark{width:30px;height:30px}

/* Large mobile banner */
.mobile{left:370px;top:225px;width:346px;height:107px;
  background:linear-gradient(90deg,var(--teal-deep) 0%,var(--teal) 55%,var(--teal-light) 72%,var(--cloud) 90%)}
.mobile .headline{left:18px;top:15px}
.mobile .headline .light{font-size:17px}
.mobile .headline .bold{font-size:19px}
.mobile .headline .gap{margin-top:8px}
.mobile .illustration{left:170px;top:6px;width:70px;height:70px}
.mobile .results{left:137px;top:33px}
.mobile .results .light{font-size:15px}
.mobile .results .bold{font-size:24px;margin-top:4px}
.mobile .cta{left:259px;top:29px;width:78px;height:22px}
.mobile .cta span{font-size:7.5px}
.mobile .brand{left:258px;top:77px;font-size:15px}
.mobile .brand .mark{width:15px;height:15px}

/* Large rectangle */
.large-rect{left:370px;top:360px;width:365px;height:303px}
.large-rect .headline{left:51px;top:25px}
.large-rect .headline .l1{font-size:26px}
.large-rect .headline .l2{font-size:32px;margin-top:4px}
.large-rect .divider{left:50px;top:103px;width:270px}
.large-rect .illustration{left:130px;top:40px;width:120px;height:120px}
.large-rect .results{left:0;top:122px;width:365px;text-align:center}
.large-rect .results .light{font-size:38px}
.large-rect .results .bold{font-size:60px;margin-top:4px}
.large-rect .cta{left:18px;top:252px;width:142px;height:37px}
.large-rect .cta span{font-size:14px}
.large-rect .brand{left:193px;top:255px;font-size:31px}
.large-rect .brand .mark{width:32px;height:32px}

/* Medium square */
.square{left:813px;top:110px;width:327px;height:326px}
.square .headline{left:26px;top:21px}
.square .headline .l1{font-size:28px}
.square .headline .l2{font-size:34px;margin-top:4px}
.square .divider{left:30px;top:101px;width:270px}
.square .illustration{left:140px;top:85px;width:120px;height:120px}
.square .results{left:0;top:118px;width:327px;text-align:center}
.square .results .light{font-size:38px}
.square .results .bold{font-size:60px;margin-top:4px}
.square .cta{left:15px;top:276px;width:132px;height:34px}
.square .cta span{font-size:13px}
.square .brand{left:178px;top:278px;font-size:28px}
.square .brand .mark{width:30px;height:30px}

/* Medium rectangle */
.medium-rect{left:820px;top:456px;width:305px;height:252px}
.medium-rect .headline{left:28px;top:16px}
.medium-rect .headline .l1{font-size:25px}
.medium-rect .headline .l2{font-size:29px;margin-top:3px}
.medium-rect .illustration{left:110px;top:40px;width:100px;height:90px}
.medium-rect .results{left:0;top:99px;width:305px;text-align:center}
.medium-rect .results .light{font-size:33px}
.medium-rect .results .bold{font-size:53px;margin-top:2px}
.medium-rect .cta{left:25px;top:209px;width:100px;height:27px}
.medium-rect .cta span{font-size:10px}
.medium-rect .brand{left:150px;top:208px;font-size:26px}
.medium-rect .brand .mark{width:28px;height:28px}
</style>
</head>
<body>

<section class="banner leaderboard" aria-label="Leaderboard banner">
  <div class="headline">
    <span class="line"><span class="light on-teal">Honest</span> <span class="bold dark">Schedule.</span></span>
    <span class="line"><span class="light on-teal">Honest</span> <span class="bold dark">Budget.</span></span>
  </div>
  <div class="v-divider"></div>
  <div class="illustration" role="img" aria-label="Rocket illustration with a rider launching through clouds"></div>
  <div class="results">
    <span class="line light dark">Outstanding</span>
    <span class="line bold dark">Results</span>
  </div>
  <div class="cta"><span class="top">Schedule</span><span class="bottom">Appointment</span></div>
  <div class="brand"><span class="mark"></span>Velquor</div>
</section>

<section class="banner half-page" aria-label="Half page banner">
  <div class="headline">
    <span class="line light on-teal">Honest</span>
    <span class="line bold on-teal">Schedule.</span>
    <span class="line light on-teal gap">Honest</span>
    <span class="line bold on-teal big">Budget.</span>
  </div>
  <div class="divider"></div>
  <div class="illustration" role="img" aria-label="Rocket illustration with a rider launching through clouds"></div>
  <div class="results">
    <span class="line light dark">Outstanding</span>
    <span class="line bold on-teal">Results</span>
  </div>
  <div class="cta"><span class="top">Schedule</span><span class="bottom">Appointment</span></div>
  <div class="brand"><span class="mark"></span>Velquor</div>
</section>

<section class="banner mobile" aria-label="Large mobile banner">
  <div class="headline">
    <span class="line light on-teal">Honest</span>
    <span class="line bold dark">Schedule.</span>
    <span class="line light on-teal gap">Honest</span>
    <span class="line bold dark">Budget.</span>
  </div>
  <div class="illustration" role="img" aria-label="Rocket illustration with a rider launching through clouds"></div>
  <div class="results">
    <span class="line light dark">Outstanding</span>
    <span class="line bold dark">Results</span>
  </div>
  <div class="cta"><span class="top">Schedule</span><span class="bottom">Appointment</span></div>
  <div class="brand"><span class="mark"></span>Velquor</div>
</section>

<section class="banner large-rect" aria-label="Large rectangle banner">
  <div class="illustration" role="img" aria-label="Rocket illustration with a rider launching through clouds"></div>
  <div class="headline">
    <span class="line l1"><span class="light on-teal">Honest</span> <span class="bold dark">Schedule.</span></span>
    <span class="line l2"><span class="light on-teal">Honest</span> <span class="bold dark">Budget.</span></span>
  </div>
  <div class="divider"></div>
  <div class="results">
    <span class="line light dark">Outstanding</span>
    <span class="line bold dark">Results</span>
  </div>
  <div class="cta"><span class="top">Schedule</span><span class="bottom">Appointment</span></div>
  <div class="brand"><span class="mark"></span>Velquor</div>
</section>

<section class="banner square" aria-label="Square banner">
  <div class="illustration" role="img" aria-label="Rocket illustration with a rider launching through clouds"></div>
  <div class="headline">
    <span class="line l1"><span class="light on-teal">Honest</span> <span class="bold dark">Schedule.</span></span>
    <span class="line l2"><span class="light on-teal">Honest</span> <span class="bold dark">Budget.</span></span>
  </div>
  <div class="divider"></div>
  <div class="results">
    <span class="line light dark">Outstanding</span>
    <span class="line bold dark">Results</span>
  </div>
  <div class="cta"><span class="top">Schedule</span><span class="bottom">Appointment</span></div>
  <div class="brand"><span class="mark"></span>Velquor</div>
</section>

<section class="banner medium-rect" aria-label="Medium rectangle banner">
  <div class="illustration" role="img" aria-label="Rocket illustration with a rider launching through clouds"></div>
  <div class="headline">
    <span class="line l1"><span class="light on-teal">Honest</span> <span class="bold dark">Schedule.</span></span>
    <span class="line l2"><span class="light on-teal">Honest</span> <span class="bold dark">Budget.</span></span>
  </div>
  <div class="results">
    <span class="line light dark">Outstanding</span>
    <span class="line bold dark">Results</span>
  </div>
  <div class="cta"><span class="top">Schedule</span><span class="bottom">Appointment</span></div>
  <div class="brand"><span class="mark"></span>Velquor</div>
</section>

</body>
</html>
```